Corp. Logo & Business Card for TRV Printing Services Ltd.

We have been in business 40 years need a stunding Corp.
Logo that shows great 3D graphics & is bright in colors so
our customers will want us to design their Corp. Logos & do their Printing. just for your information, I like Colors Maroon,
Yellow, Red etc. You do not have to stay with these colors if you have a better color design. The TRV Logo I would like a Very distinctive Font & can be Mulit Color.
I have attached what we are using now, I like the Red Gold with the bright sun light
behind the copy to attach attention.

TRV
Printing Services Ltd.
P.O. Box 4362, Brea, CA 92819
714.389.5140 ext. 316
714.389.5163 Fax
marv @ inkharborworks.com
www.trvinkharborprinting.com

TRV
Printing Services Ltd.
714.389.5140 ext. 316
714.389.5163 Fax

Dear Designers; You all did a great job.

Thanks

Marv Delbrook

```html
<!DOCTYPE html>
<html lang="en">
<head>
<meta charset="utf-8">
<title>TRV Printing Services Ltd – Business Card</title>
<link rel="stylesheet" href="https://fonts.googleapis.com/css2?family=Exo+2:wght@400;600;700&display=swap">
<style>
  :root {
    --stage: #2b2b2b;
    --maroon: #5e0a30;
    --pink: #e01e63;
    --blue: #1e8fd6;
    --paper: #ececec;
  }
  * { margin: 0; padding: 0; box-sizing: border-box; }
  html, body { width: 1200px; height: 900px; overflow: hidden; }
  body {
    background: var(--stage);
    font-family: "Exo 2", sans-serif;
    position: relative;
  }
  .card {
    position: absolute;
    width: 500px;
    height: 286px;
    overflow: hidden;
    box-shadow: 0 10px 30px rgba(0,0,0,.5);
  }
  /* Front */
  .card-front { left: 70px; top: 307px; background: var(--maroon); }
  .front-disc {
    position: absolute;
    left: 40px; top: -60px;
    width: 230px; height: 230px;
    border-radius: 50%;
    background: var(--pink);
    opacity: .9;
  }
  .front-name {
    position: absolute;
    left: 40px; top: 190px;
    color: var(--pink);
    font-weight: 700;
    font-size: 30px;
    line-height: 1.05;
    letter-spacing: .5px;
  }
  /* Back */
  .card-back { left: 630px; top: 307px; background: var(--paper); }
  .brand {
    position: absolute;
    left: 30px; top: 34px;
    display: flex; align-items: center; gap: 10px;
  }
  .brand-dot { width: 26px; height: 26px; border-radius: 50%; background: var(--pink); }
  .brand-name {
    color: var(--pink);
    font-weight: 700;
    font-size: 19px;
    line-height: 1.05;
  }
  .person {
    position: absolute;
    left: 30px; top: 112px;
    color: var(--blue);
    font-weight: 600;
    font-size: 17px;
    letter-spacing: .5px;
    text-transform: uppercase;
  }
  .address {
    position: absolute;
    left: 30px; top: 142px;
    color: var(--pink);
    font-size: 11.5px;
    line-height: 1.35;
  }
  .contact {
    position: absolute;
    right: 24px; top: 168px;
    font-size: 11.5px;
    line-height: 1.35;
    color: var(--pink);
  }
  .contact .phone { color: var(--blue); }
  .band {
    position: absolute; bottom: 0; height: 18px;
  }
  .band-pink { left: 0; width: 45%; background: var(--pink); }
  .band-blue { left: 45%; right: 0; background: var(--blue); }
</style>
</head>
<body>
  <section class="card card-front" aria-label="Card front">
    <div class="front-disc"></div>
    <p class="front-name">TRV Printing<br>Services Ltd</p>
  </section>

  <section class="card card-back" aria-label="Card back">
    <div class="brand">
      <span class="brand-dot"></span>
      <span class="brand-name">TRV Printing<br>Services Ltd</span>
    </div>
    <h1 class="person">Marv Delbrook</h1>
    <p class="address">P.O. Box 4362, Brea,<br>CA 92819</p>
    <p class="contact">
      <span class="phone">PH: 714.389.5140 ext. 316</span><br>
      <span class="phone">FAX: 714.389.5163</span><br>
      marv @ inkharborworks.com<br>
      www.trvinkharborprinting.com
    </p>
    <div class="band band-pink"></div>
    <div class="band band-blue"></div>
  </section>
</body>
</html>
```